specialised legal consultancy business needs an update on logo and office stationary.

Update on Logo - see attached.

update on email signature - something new and fresh with only the following details -

(the logo)
Advocate Peter Sandovik
PS Entity Frameworks (Pty) Ltd (Reg No.: 2019 / 153927 / 07)
LLB, LLM (Cum Laude), Cert.Dir (KWBFE), FCG (TREPX)
+27 71 592 6604
peter#kwellbrandt.com

Update on letterhead - something new and fresh and please more user-friendly. With the same details as per the email signature.

```html
<!DOCTYPE html>
<html lang="en">
<head>
<meta charset="utf-8">
<title>PS Frameworks Letterhead</title>
<link href="https://fonts.googleapis.com/css2?family=Arimo:wght@400;700&family=Open+Sans:wght@600;700&display=swap" rel="stylesheet">
<style>
  :root {
    --backdrop: #94979b;
    --paper: #ffffff;
    --paper-shade: #efefef;
    --ink: #111111;
    --text: #4a4a4a;
    --muted: #6f6f6f;
    --rule: #555555;
    --faint: #ececec;
  }
  * { box-sizing: border-box; margin: 0; padding: 0; }
  html, body { width: 1200px; height: 1200px; overflow: hidden; }
  body { background: var(--backdrop); position: relative; font-family: "Arimo", Arial, sans-serif; }

  .letterhead {
    position: absolute; left: 204px; top: 40px;
    width: 792px; height: 1120px;
    background: linear-gradient(158deg, var(--paper-shade) 0%, var(--paper) 42%);
    overflow: hidden;
  }

  .brand { position: absolute; left: 71px; top: 36px; width: 122px; text-align: center; }
  .brand-square { width: 64px; height: 64px; background: var(--ink); margin: 16px auto 24px; }
  .brand-name {
    font-family: "Open Sans", Arial, sans-serif; font-weight: 700;
    font-size: 12.5px; letter-spacing: 1.2px; color: var(--ink); white-space: nowrap;
  }
  .brand-tagline {
    font-family: "Open Sans", Arial, sans-serif; font-weight: 700;
    font-size: 4.5px; letter-spacing: 1.6px; color: var(--muted); margin-top: 3px; white-space: nowrap;
  }

  .contact {
    position: absolute; left: 530px; top: 53px;
    border-left: 1px solid var(--rule); padding-left: 13px;
    font-size: 12.5px; line-height: 15.5px; color: var(--muted);
  }
  .contact-line { display: flex; align-items: center; gap: 6px; }
  .contact-line.spaced { margin-top: 4px; }
  .contact svg { width: 9px; height: 9px; fill: #333; flex: none; }

  .letter { position: absolute; left: 71px; top: 344px; width: 650px; }
  .salutation {
    font-family: "Open Sans", Arial, sans-serif; font-weight: 600;
    font-size: 17.5px; color: var(--text); margin-bottom: 26px;
  }
  .letter p { font-size: 13.4px; line-height: 16.2px; color: var(--text); margin-bottom: 15px; }
  .closing { font-size: 10px; font-weight: 700; color: var(--text); margin-top: 26px; }
  .signature {
    width: 130px; height: 40px; margin-top: 26px;
    background: linear-gradient(90deg, #d9d9d9, #eeeeee);
  }

  .decor {
    position: absolute; left: 461px; top: 740px; width: 331px; height: 380px;
    background: linear-gradient(180deg, rgba(236,236,236,0) 0%, var(--faint) 55%);
  }
</style>
</head>
<body>
  <main class="letterhead">
    <header>
      <div class="brand">
        <div class="brand-square"></div>
        <div class="brand-name">PS FRAMEWORKS</div>
        <div class="brand-tagline">LEGAL CONSULTANCY</div>
      </div>
      <address class="contact" style="font-style:normal">
        <div>Reg No.: 2019 / 153927 / 07)</div>
        <div>LLB, LLM (Cum Laude)</div>
        <div>Cert.Dir (KWBFE), FCG (TREPX)</div>
        <div class="contact-line spaced">
          <svg viewBox="0 0 24 24" aria-hidden="true"><path d="M6.6 10.8a15.1 15.1 0 0 0 6.6 6.6l2.2-2.2c.3-.3.7-.4 1-.2 1.1.4 2.3.6 3.6.6.6 0 1 .4 1 1V20c0 .6-.4 1-1 1A17 17 0 0 1 3 4c0-.6.4-1 1-1h3.5c.6 0 1 .4 1 1 0 1.3.2 2.5.6 3.6.1.3 0 .7-.2 1z"/></svg>
          <span>+27 71 592 6604</span>
        </div>
        <div class="contact-line">
          <svg viewBox="0 0 24 24" aria-hidden="true"><path d="M2 5h20v14H2z M2 5l10 8 10-8" /></svg>
          <span>peter#kwellbrandt.com</span>
        </div>
      </address>
    </header>

    <section class="letter">
      <h1 class="salutation">Dear Mr. Halvorsen,</h1>
      <p>Lorem ipsum dolor sit amet, consectetuer adipiscing elit, sed diam nonmmy nibh euismod tincidunt ut laor eet dolore magna aliquam erat volutpat. Ut wisi enim ad minim veniam, quis nostrud exerci tationmcorper suscipit lobortis nisl ut aliquip ex ea commodo consequat. Duis autem vel eum iriure dolor in hendrerit in vulputate velit esse molestie consequat, vel illum dolore eu feugiat</p>
      <p>Rorem ipsum dolor sit amet, consectetuer adipiscing elit, sed diam nonmmy nibh euismod tincidunt ut laor eet dolore magna aliquam erat volutpat. Ut wisi enim ad minim veniam, quis nostrud exerci tationmcorper suscipit lobortis nisl ut aliquip ex ea commodo consequat. Duis autem vel eum iriure dolor in hendrerit in vulputate velit esse molest</p>
      <p>Dorem ipsum dolor sit amet, consectetuer adipiscing elit, sed diam nonmmy nibh euismod tincidunt ut laor eet dolore magna aliquam erat volutpat. Ut wisi enim ad minim veniam, quis nostrud exerci tationmcorper suscipit lobortis nisl ut aliquip ex ea commodo consequat. Duis autem vel eum iriure dolor in hendrerit in suscipit lobortis nisl ut aliquip ex ea commodo consequat. Duis autem vel eum iriure dolor in hendrerit in vulputate velit esse molestie consequat, vel illum</p>
      <p>Sorem ipsum dolor sit amet, consectetuer adipiscing elit, sed diam nonmmy nibh euismod tincidunt ut laor eet dolore magna aliquam erat volutpat. Ut wisi enim ad minim veniam, quis nostrud exerci tationmcorper suscipit lobortis nisl ut aliquip ex ea commodo consequat. Duis autem vel eum iriure dolor in</p>
      <div class="closing">Sincerely,</div>
      <div class="signature" role="img" aria-label="Handwritten signature of the sender"></div>
    </section>

    <div class="decor" role="img" aria-label="Faint oversized brand decoration in the lower right corner"></div>
  </main>
</body>
</html>
```